Fitness & sports performance company needs a landing page design

Looking for a landing page for a fitness & sports performance company based in Bayside District. The company is 'The Larkfield Fitness Studio', and 'The Larkfield' for short. The main objective of the landing page is to generate leads, and show potential clients the services we offer, as well as pricing for each service. While we are based in Bayside District, we also offer online services such as an online trainer and online strength & conditioning programs. Would like to see designs that utilize the colors in our logo.

Target Market(s)

those looking to lose weight, gain strength and make overall healthy lifestyle changes

Font styles to use
Sans Serif

Colors
60b9df
57b5de

Requirements
Must have
• a place to list testimonials, list of services provided, show pricing for each service, colors of the website matching colors in the logo
Nice to have
• i would like to see a landing page that can be utilized to create leads and an email list

```html
<!DOCTYPE html>
<html lang="en">
<head>
<meta charset="utf-8">
<title>The Larkfield Fitness Studio</title>
<link rel="stylesheet" href="https://fonts.googleapis.com/css2?family=Montserrat:wght@400;500;600;700&family=Ubuntu:wght@500;700&display=swap">
<style>
:root{
  --page:#595959;
  --ink-dark:#15181c;
  --brand:#5bb7df;
  --brand-deep:#4aa6cf;
  --white:#ffffff;
  --card:#f8f8f8;
  --text:#222222;
  --coral:#ef6b5f;
  --teal:#5fc3bf;
  --night:#13263a;
}
*{box-sizing:border-box;margin:0;padding:0}
html,body{width:1200px;height:1200px;overflow:hidden;background:var(--page);font-family:"Montserrat",sans-serif;color:var(--white)}
.canvas{position:relative;width:1200px;height:1200px;overflow:hidden}
.abs{position:absolute}

/* hero */
.hero{left:216px;top:0;width:768px;height:334px;background:var(--ink-dark)}
.hero-photo{left:400px;top:0;width:368px;height:334px;background:radial-gradient(ellipse at 60% 45%,#8a6a58 0%,#4a3a33 35%,#1e1d20 75%,#15181c 100%)}
.nav-band{left:0;top:62px;width:768px;height:48px;border-top:1px solid #262a2f;border-bottom:1px solid #262a2f;background:rgba(10,12,15,.35)}
.brand{left:344px;top:8px;width:80px;text-align:center}
.brand-dot{width:44px;height:44px;border-radius:50%;background:var(--brand);margin:0 auto}
.brand-name{font-size:8px;font-weight:600;margin-top:2px;color:var(--white)}
.nav{top:80px;left:182px;display:flex;gap:34px;font-size:12.5px;font-weight:700}
.social{top:77px;left:512px;display:flex;gap:5px}
.social span{width:19px;height:19px;border-radius:50%;background:var(--white);border:2px solid #222}
.hero-kicker{left:104px;top:150px;font-size:17px;font-weight:400}
.hero-title{left:104px;top:170px;font-size:27px;font-weight:700;letter-spacing:.3px}
.hero-title em{font-style:normal;color:var(--brand)}
.hero-copy{left:106px;top:205px;width:284px;font-size:8.5px;line-height:9.6px}
.btn{top:259px;height:31px;border-radius:16px;font-size:10px;font-weight:500;display:flex;align-items:center;justify-content:center;width:104px}
.btn-solid{left:107px;background:var(--brand)}
.btn-ghost{left:219px;border:2px solid var(--brand)}

/* motivation */
.section-title{left:0;width:1200px;top:354px;text-align:center;font-size:18px;font-weight:600}
.title-rule{left:548px;top:388px;width:104px;height:3px;background:var(--brand)}
.quote{left:292px;top:407px;width:616px;text-align:center;font-size:10px;line-height:11.6px;font-weight:600;text-transform:uppercase}

/* services */
.services-band{left:215px;top:494px;width:768px;height:200px;background:#1b2028}
.services-photo{left:340px;top:0;width:428px;height:200px;background:radial-gradient(ellipse at 45% 55%,#9a7560 0%,#5a4438 40%,#262a30 80%,#1b2028 100%)}
.svc-kicker{left:296px;top:506px;font-size:19px}
.svc-title{left:296px;top:546px;font-size:27px;font-weight:700}
.svc-title em{font-style:normal;color:var(--brand)}
.card{width:320px;height:160px;background:var(--card);border-radius:3px;color:var(--text);text-align:center}
.card h3{font-family:"Ubuntu",sans-serif;font-weight:700;font-size:13.5px;margin-top:46px}
.card p{font-size:9.5px;line-height:11.6px;margin:11px 16px 0}
.price{font-family:"Ubuntu",sans-serif;font-weight:700;font-size:14px;margin-top:6px}
.price b{color:var(--brand);font-weight:700}
.avatar{width:64px;height:64px;border-radius:50%;border:2px solid var(--white);background:linear-gradient(160deg,#c9d4de,#6b7f95 60%,#3a4450)}

/* contact */
.find{left:216px;top:966px;width:768px;height:234px;background:linear-gradient(100deg,#1a3b57 0%,#13263a 45%,#0f1f30 70%,#1a3a55 100%)}
.find-title{left:329px;top:990px;font-size:19px;font-weight:700}
.find-rule{left:329px;top:1024px;width:16px;height:3px;background:var(--brand)}
.info{left:376px;font-size:10.5px;font-weight:600;line-height:11.5px}
.info span{display:block;color:var(--brand);font-weight:500}
.icon{left:326px}

.member{left:640px;top:995px;width:221px;height:193px;background:var(--white);border:3px solid var(--teal);border-radius:6px;color:var(--text)}
.member h4{font-weight:400;font-size:11px;text-align:center;padding:14px 0 12px;background:#f3f3f3}
.field{position:absolute;left:22px;width:174px;height:28px;background:#f4f4f4;font-size:6px;color:#bbb;padding:10px 0 0 40px}
.mbtn{position:absolute;left:22px;width:175px;height:25px;border-radius:3px;font-size:8.5px;color:var(--white);display:flex;align-items:center;justify-content:center}
</style>
</head>
<body>
<div class="canvas">

  <header class="abs hero">
    <div class="abs hero-photo" role="img" aria-label="Photo of a female athlete in a dark gym"></div>
    <div class="abs nav-band"></div>
    <div class="abs brand">
      <div class="brand-dot"></div>
      <div class="brand-name">The Larkfield</div>
    </div>
    <nav class="abs nav"><span>Home</span><span>Blog</span><span>Services</span><span>Contact us</span></nav>
    <div class="abs social" aria-label="Social links"><span></span><span></span><span></span><span></span></div>
    <div class="abs hero-kicker">Looking for</div>
    <h1 class="abs hero-title">PERSONAL <em>TRAINER?</em></h1>
    <p class="abs hero-copy">Lorem ipsum dolor sit amet, consectetur adipiscing elit, sed do eiusmod tempor incididunt ut labore et dolore magna aliqua. Ut enim ad minim veniam, quis nostrud exercitation ullamco laboris nisi ut aliquip ex ea commodo consequat.</p>
    <div class="abs btn btn-solid">GET STARTED</div>
    <div class="abs btn btn-ghost">MORE INFO</div>
  </header>

  <h2 class="abs section-title">THE MOTIVATION</h2>
  <div class="abs title-rule"></div>
  <p class="abs quote">"Lorem ipsum dolor sit amet, consectetur adipiscing elit, sed do eiusmod tempor incididunt ut labore et dolore magna aliqua. Ut enim ad minim veniam, quis nostrud exercitation ullamco laboris nisi ut aliquip ex ea commodo consequat. Duis aute irure dolor in reprehenderit in voluptate velit esse cillum dolore eu fugiat nulla pariatur. Excepteur sint occaecat cupidatat non proident, sunt in culpa qui officia deserunt mollit anim id est laborum."</p>

  <section class="abs services-band">
    <div class="abs services-photo" role="img" aria-label="Photo of an athlete's muscular back in a gym"></div>
  </section>
  <div class="abs svc-kicker">Training</div>
  <h2 class="abs svc-title"><em>SERVICES</em> WE OFFER</h2>

  <div class="abs card" style="left:264px;top:606px"><h3>Service Name</h3><p>Lorem ipsum dolor sit amet, consectetur adipiscing elit. Cras tincidunt orci ut suscipit pretium. Class aptent taciti sociosqu ad litora torquent per conubia nostra, per inceptos himenaeos</p><div class="price">$ <b>25</b>/mon</div></div>
  <div class="abs card" style="left:615px;top:606px"><h3>Service Name</h3><p>Lorem ipsum dolor sit amet, consectetur adipiscing elit. Cras tincidunt orci ut suscipit pretium. Class aptent taciti sociosqu ad litora torquent per conubia nostra, per inceptos himenaeos</p><div class="price">$ <b>50</b>/mon</div></div>
  <div class="abs card" style="left:264px;top:798px"><h3>Service Name</h3><p>Lorem ipsum dolor sit amet, consectetur adipiscing elit. Cras tincidunt orci ut suscipit pretium. Class aptent taciti sociosqu ad litora torquent per conubia nostra, per inceptos himenaeos</p><div class="price">$ <b>100</b>/mon</div></div>
  <div class="abs card" style="left:615px;top:798px"><h3>Service Name</h3><p>Lorem ipsum dolor sit amet, consectetur adipiscing elit. Cras tincidunt orci ut suscipit pretium. Class aptent taciti sociosqu ad litora torquent per conubia nostra, per inceptos himenaeos</p><div class="price">$ <b>150</b>/mon</div></div>

  <div class="abs avatar" style="left:392px;top:577px" role="img" aria-label="Photo of a trainer working with a client"></div>
  <div class="abs avatar" style="left:743px;top:577px" role="img" aria-label="Photo of a coach in a gym"></div>
  <div class="abs avatar" style="left:392px;top:769px" role="img" aria-label="Photo of a trainer working with a client"></div>
  <div class="abs avatar" style="left:743px;top:769px" role="img" aria-label="Photo of a coach in a gym"></div>

  <section class="abs find" role="img" aria-label="Dim blue-toned photo of an athlete training"></section>
  <h2 class="abs find-title">HOW &amp; WHERE TO FIND US</h2>
  <div class="abs find-rule"></div>

  <svg class="abs icon" style="top:1052px" width="20" height="26" viewBox="0 0 20 26" fill="none" stroke="#fff" stroke-width="1.4"><path d="M10 25C10 25 2 15 2 9a8 8 0 0 1 16 0c0 6-8 16-8 16z"/><circle cx="10" cy="9" r="3"/></svg>
  <div class="abs info" style="top:1055px">LOCATION<span>BAYSIDE DISTRICT</span></div>

  <svg class="abs icon" style="top:1106px" width="22" height="22" viewBox="0 0 22 22" fill="none" stroke="#fff" stroke-width="1.3"><path d="M4 2l4 4-2 3c1 3 4 6 7 7l3-2 4 4-3 3C9 21 1 13 1 5z"/></svg>
  <div class="abs info" style="top:1107px">PHONE NUMBER<span>305 555 014</span></div>

  <svg class="abs icon" style="top:1152px" width="24" height="22" viewBox="0 0 24 22" fill="none" stroke="#fff" stroke-width="1.3"><path d="M2 8h20v13H2z"/><path d="M2 8l10 7 10-7"/><path d="M2 21l8-6M22 21l-8-6"/><path d="M6 8V2h12v6"/></svg>
  <div class="abs info" style="top:1155px">EMAIL<span>hello@larkfieldstudio.com</span></div>

  <aside class="abs member">
    <h4>Membership</h4>
    <div class="field" style="top:55px">username</div>
    <div class="field" style="top:84px">password</div>
    <div class="mbtn" style="top:120px;background:var(--coral)">&gt;&nbsp; Sign Up</div>
    <div class="mbtn" style="top:148px;background:var(--brand)">+&nbsp; Already Have a Account</div>
  </aside>

</div>
</body>
</html>
```